Website Required for Small Cyber Security Company

Require a website for Cyber Security company. I have logo which i will attach. Please use logo blue and white as a guide
Would ultimately like the site to have a technology theme with the following pages Landing page
Services
Contact
Careers

I can provide content for each of those pages in due course, until then happy for you to use dummy data to display purposes

Target Market(s)

Government

Industry/Entity Type

Cyber Security

Coding

Coded - Design and coding required

Number of Pages Required

4 page

Colors
0054AA
0677BA
7BADD7
CADEEF
E8F1F8

Requirements
Must have
• High quality finish and UX
Nice to have
• look and feel professional and not cheap

```html
<!DOCTYPE html>
<html lang="en">
<head>
<meta charset="utf-8">
<title>Harlow Ridge — Cyber Security</title>
<link href="https://fonts.googleapis.com/css2?family=Montserrat:wght@400;500;600;700;800&family=Poppins:wght@300;400;500;600&display=swap" rel="stylesheet">
<style>
:root{
  --blue-deep:#0a2a78;
  --blue-navy:#0b3a9c;
  --blue:#0054AA;
  --blue-mid:#0677BA;
  --blue-soft:#7BADD7;
  --blue-pale:#CADEEF;
  --blue-mist:#E8F1F8;
  --white:#ffffff;
  --ink:#1b2a4a;
  --grey:#5b667a;
  --line:#d4dbe6;
}
*{box-sizing:border-box;margin:0;padding:0}
html,body{width:1200px;height:4056px;overflow:hidden}
body{position:relative;font-family:"Poppins",sans-serif;color:var(--ink);background:var(--white)}
h1,h2,h3,h4,.brand,.btn{font-family:"Montserrat",sans-serif}
.abs{position:absolute}

/* Hero */
.hero{position:absolute;left:0;top:0;width:1200px;height:920px;background:linear-gradient(135deg,#0a2f8e 0%,#0054AA 45%,#0677BA 100%);overflow:hidden}
.hero-art{position:absolute;left:470px;top:40px;width:730px;height:720px;background:radial-gradient(ellipse at 55% 45%,#3fb3f0 0%,#1a78cf 35%,rgba(6,119,186,0) 70%)}
.hero-curve{position:absolute;left:0;top:0;width:1200px;height:920px}
.nav{position:absolute;left:0;top:0;width:1200px;height:110px}
.brand{position:absolute;left:160px;top:58px;display:flex;align-items:center;gap:14px;color:var(--white);font-size:30px;font-weight:700;letter-spacing:1px;white-space:nowrap}
.brand .dot{width:34px;height:34px;border:3px solid var(--white);border-radius:50%}
.menu{position:absolute;right:160px;top:44px;display:flex;gap:36px;list-style:none}
.menu a{color:var(--white);text-decoration:none;font:600 15px "Montserrat",sans-serif;letter-spacing:.5px}
.hero-copy{position:absolute;left:160px;top:330px;color:var(--white)}
.hero-copy h1{font-size:40px;font-weight:800;letter-spacing:1px}
.hero-copy h2{font-size:28px;font-weight:700;line-height:1.2;margin-top:6px}
.btn{display:inline-flex;align-items:center;gap:8px;font-size:13px;font-weight:700;text-decoration:none;border-radius:3px;padding:10px 22px;white-space:nowrap}
.btn-light{background:var(--white);color:var(--blue)}
.btn-blue{background:var(--blue-mid);color:var(--white)}
.hero-copy .btn{margin-top:24px}

/* Why */
.why{position:absolute;left:0;top:735px;width:1200px;text-align:center}
.why h2{font-size:38px;font-weight:700;color:var(--blue-navy)}
.why p.lead{width:760px;margin:10px auto 0;font-size:14px;color:var(--grey);line-height:1.5}
.why-card{position:absolute;top:860px;width:256px;height:316px;background:var(--white);box-shadow:0 6px 26px rgba(10,40,110,.16);text-align:center;padding:40px 24px 0}
.why-card.featured{background:linear-gradient(180deg,#0054AA,#0a2f8e);color:var(--white);top:848px;height:340px}
.why-card h3{font-size:15px;font-weight:700;margin-top:20px;white-space:nowrap}
.why-card p{font-size:13px;line-height:1.5;margin-top:14px;color:var(--grey)}
.why-card.featured p{color:var(--blue-pale)}
.why-card .btn{position:absolute;left:50%;bottom:34px;transform:translateX(-50%)}
.icon{width:70px;height:70px;margin:0 auto}

/* Services */
.services{position:absolute;left:0;top:1240px;width:1200px;height:990px;background:radial-gradient(ellipse at 55% 60%,#1c7fd6 0%,#0054AA 45%,#0a2a78 100%)}
.sec-head{position:absolute;display:flex;gap:24px;align-items:flex-start;color:var(--white)}
.sec-head .ring{width:110px;height:110px;border:4px solid rgba(255,255,255,.6);border-radius:50%;flex:none}
.sec-head h2{font-size:34px;font-weight:700;letter-spacing:1px}
.sec-head p{font-size:15px;line-height:1.5;margin-top:8px;color:var(--blue-pale);width:420px}
.svc{position:absolute;background:var(--white);border:6px solid var(--blue-pale);box-shadow:0 0 0 2px rgba(255,255,255,.4),0 10px 30px rgba(0,0,0,.25);padding:26px 26px}
.svc h3{font-size:16px;font-weight:700;color:var(--blue-navy);margin-top:14px}
.svc p{font-size:13px;line-height:1.5;color:var(--grey);margin-top:10px}
.svc .more{position:absolute;left:26px;bottom:22px;font:700 12px "Montserrat",sans-serif;color:var(--ink);display:flex;gap:8px;align-items:center}
.svc .more i{width:12px;height:12px;border-radius:50%;background:var(--blue);display:inline-block}
.svc-icon{width:56px;height:56px}

/* About */
.about-pattern{position:absolute;left:160px;top:2262px;width:440px;height:460px;background:radial-gradient(circle at 30% 30%,#f1f4f8,#e3e8ef);border:1px solid var(--line)}
.about-left{position:absolute;left:250px;top:2390px;width:260px}
.about-left h2{font-size:26px;font-weight:700;color:var(--blue-navy);display:flex;align-items:center;gap:14px}
.about-left h2:before{content:"";width:60px;height:3px;background:var(--blue-navy)}
.about-left p{font-size:15px;color:var(--grey);line-height:1.5;margin-top:24px}
.about-card{position:absolute;left:600px;top:2272px;width:448px;height:488px;background:var(--white);border:1px solid var(--line);box-shadow:0 10px 30px rgba(10,40,110,.15);padding:30px 40px 0 86px}
.about-card p{font-size:13px;color:var(--grey);line-height:1.55;margin-bottom:18px}
.about-card .btn{position:absolute;right:40px;bottom:34px}
.about-ring{position:absolute;left:528px;top:2384px;width:144px;height:144px;border-radius:50%;background:var(--white);border:5px solid var(--blue-mid)}

/* Feedback */
.feedback{position:absolute;left:0;top:2790px;width:1200px;height:480px;background:linear-gradient(135deg,#0a2f8e,#0054AA 55%,#0677BA)}
.quote{position:absolute;top:160px;width:268px;height:300px;background:var(--white);box-shadow:0 10px 26px rgba(0,0,0,.2);text-align:center;padding:108px 30px 0}
.quote .photo{position:absolute;left:84px;top:-10px;width:100px;height:100px;border-radius:50%;background:linear-gradient(160deg,#c9d4e2,#7BADD7);border:4px solid var(--white)}
.quote p{font-size:13px;color:var(--grey);line-height:1.55}
.quote h4{font-size:14px;color:var(--blue);margin-top:14px;font-weight:700}

/* Contact */
.contact{position:absolute;left:0;top:3270px;width:1200px;height:562px;background:linear-gradient(180deg,#eef3f8,#f7f9fc)}
.contact h2{position:absolute;left:0;top:50px;width:1200px;text-align:center;font-size:30px;font-weight:700;color:var(--blue-navy);letter-spacing:1px}
.field{position:absolute}
.field label{font-size:12px;color:var(--grey)}
.field span{display:block;margin-top:6px;height:44px;background:var(--white);border:1px solid var(--line)}
.contact .btn{position:absolute;left:516px;top:462px;width:168px;justify-content:center;background:var(--blue);color:var(--white);font-size:15px;padding:12px 0}

/* Footer */
.footer{position:absolute;left:0;top:3832px;width:1200px;height:224px;background:linear-gradient(135deg,#0a2f8e,#0054AA);color:var(--white)}
.footer .brand{left:160px;top:52px;font-size:26px}
.footer h4{font-size:15px;font-weight:700}
.footer p{font-size:13px;line-height:1.5;color:var(--blue-pale);margin-top:8px}
.social{display:flex;gap:10px;margin-top:14px}
.social i{width:30px;height:30px;border:2px solid var(--white);border-radius:50%;display:block}
.copy{position:absolute;left:160px;top:190px;font-size:11px;color:var(--blue-pale)}
</style>
</head>
<body>

<header class="hero">
  <div class="hero-art" role="img" aria-label="Illustration of a smartphone surrounded by glowing padlocks, shields and circuit lines"></div>
  <svg class="hero-curve" viewBox="0 0 1200 920" aria-hidden="true">
    <path d="M0 690 C 300 710, 560 790, 760 710 C 920 640, 1060 550, 1200 590 L1200 920 L0 920 Z" fill="#ffffff"/>
    <path d="M0 680 C 300 700, 560 780, 760 700 C 920 630, 1060 540, 1200 580" fill="none" stroke="#7BADD7" stroke-width="3" opacity=".7"/>
  </svg>
  <nav class="nav">
    <div class="brand"><span class="dot"></span>HARLOW RIDGE</div>
    <ul class="menu">
      <li><a href="#">HOME</a></li>
      <li><a href="#">SERVICES</a></li>
      <li><a href="#">CONTACT</a></li>
      <li><a href="#">CAREERS</a></li>
    </ul>
  </nav>
  <div class="hero-copy">
    <h1>CYBER SECURITY</h1>
    <h2>WE'RE PROTECTING YOUR<br>BUSINESS AS WELL.</h2>
    <a class="btn btn-light" href="#">CONTACT US →</a>
  </div>
</header>

<section class="why">
  <h2>Why Choose Harlow Ridge</h2>
  <p class="lead">Many desktop publishing packages and web page editors now use sample text as their default model text, and a search for filler text will uncover many sites in their infancy.</p>
</section>

<article class="why-card" style="left:176px">
  <svg class="icon" viewBox="0 0 70 70"><circle cx="24" cy="24" r="12" fill="none" stroke="#0054AA" stroke-width="4"/><circle cx="46" cy="46" r="12" fill="none" stroke="#0677BA" stroke-width="4"/><path d="M40 14h16v16M30 56H14V40" fill="none" stroke="#0054AA" stroke-width="4"/></svg>
  <h3>Actionable Intelligence</h3>
  <p>It is a long established fact that a reader will be distracted.</p>
  <a class="btn btn-blue" href="#">CONTACT US →</a>
</article>
<article class="why-card featured" style="left:472px">
  <svg class="icon" viewBox="0 0 70 70"><circle cx="35" cy="35" r="26" fill="none" stroke="#fff" stroke-width="4"/><circle cx="35" cy="35" r="14" fill="none" stroke="#fff" stroke-width="4"/><circle cx="35" cy="35" r="4" fill="#fff"/><path d="M35 35 L60 10" stroke="#fff" stroke-width="4"/></svg>
  <h3>Assurance of accuracy</h3>
  <p>It is a long established fact that a reader will be distracted.</p>
  <a class="btn btn-light" href="#">CONTACT US →</a>
</article>
<article class="why-card" style="left:768px">
  <svg class="icon" viewBox="0 0 70 70"><rect x="8" y="12" width="54" height="38" rx="3" fill="none" stroke="#0054AA" stroke-width="4"/><path d="M24 60h22M35 50v10" stroke="#0054AA" stroke-width="4"/><circle cx="35" cy="31" r="9" fill="none" stroke="#0677BA" stroke-width="4"/></svg>
  <h3>Automation of processes</h3>
  <p>It is a long established fact that a reader will be distracted.</p>
  <a class="btn btn-blue" href="#">CONTACT US →</a>
</article>

<section class="services">
  <div class="sec-head" style="left:160px;top:70px">
    <span class="ring"></span>
    <div>
      <h2>OUR SERVICES</h2>
      <p>It is a long established fact that a reader will be distracted by the readable content of a page when looking at its layout.</p>
    </div>
  </div>

  <article class="svc" style="left:160px;top:228px;width:580px;height:290px">
    <svg class="svc-icon" viewBox="0 0 56 56"><path d="M6 22 L28 8 L50 22Z" fill="#0054AA"/><path d="M12 26v16M22 26v16M34 26v16M44 26v16" stroke="#0054AA" stroke-width="4"/><rect x="6" y="44" width="44" height="5" fill="#0054AA"/></svg>
    <h3>BANKING SECURITY</h3>
    <p>It is a long established fact that a reader will be distracted by the readable content of a page when looking at its layout.</p>
    <span class="more"><i></i>READ MORE</span>
  </article>

  <article class="svc" style="left:780px;top:140px;width:268px;height:330px">
    <svg class="svc-icon" viewBox="0 0 56 56"><rect x="6" y="14" width="44" height="30" rx="2" fill="none" stroke="#0054AA" stroke-width="4"/><path d="M6 16 L28 32 L50 16" fill="none" stroke="#0054AA" stroke-width="4"/></svg>
    <h3>EMAIL SECURITY</h3>
    <p>It is a long established fact that a reader will be distracted by the readable content of a page when looking at its layout.</p>
    <span class="more"><i></i>READ MORE</span>
  </article>

  <article class="svc" style="left:160px;top:550px;width:300px;height:330px">
    <svg class="svc-icon" viewBox="0 0 56 56"><rect x="6" y="8" width="44" height="40" rx="3" fill="none" stroke="#0054AA" stroke-width="4"/><path d="M6 18h44" stroke="#0054AA" stroke-width="4"/><rect x="20" y="26" width="16" height="14" fill="#0677BA"/></svg>
    <h3>DATA LOSS PREVENTION</h3>
    <p>Took a galley of type and scrambled it to make a type specimen book. It has survived not only five centuries, but also the leap into.</p>
    <span class="more"><i></i>READ MORE</span>
  </article>
  <article class="svc" style="left:472px;top:550px;width:296px;height:330px">
    <svg class="svc-icon" viewBox="0 0 56 56"><path d="M14 40a10 10 0 0 1 2-20 14 14 0 0 1 26 4 8 8 0 0 1 0 16Z" fill="#0054AA"/><rect x="23" y="26" width="10" height="9" fill="#fff"/></svg>
    <h3>CLOUD SECURITY</h3>
    <p>Took a galley of type and scrambled it to make a type specimen book. It has survived not only five centuries, but also the leap into.</p>
    <span class="more"><i></i>READ MORE</span>
  </article>
  <article class="svc" style="left:780px;top:550px;width:268px;height:330px">
    <svg class="svc-icon" viewBox="0 0 56 56"><circle cx="28" cy="28" r="14" fill="none" stroke="#0054AA" stroke-width="4"/><path d="M28 6v8M28 42v8M6 28h8M42 28h8M12 12l6 6M38 38l6 6M44 12l-6 6M12 44l6-6" stroke="#0054AA" stroke-width="4"/></svg>
    <h3>WEB SECURITY</h3>
    <p>Took a galley of type and scrambled it to make a type specimen book. It has survived not only five centuries, but also the leap into.</p>
    <span class="more"><i></i>READ MORE</span>
  </article>
</section>

<div class="about-pattern" role="img" aria-label="Faint grey network of connected dots"></div>
<section class="about-left">
  <h2>About</h2>
  <p>Lorem ipsum is that it has a more-or-less normal distribution of letters, as opposed to using.</p>
</section>
<article class="about-card">
  <p>It is a long established fact that a reader will be distracted by the readable content of a page when looking at its layout. The point of using sample text is that it has a more-or-less normal distribution of letters, as opposed to using placeholder text, making it look like readable English.</p>
  <p>Many desktop publishing packages and web page editors now use sample text as their default model text, and a search for filler text will uncover many web sites still in their infancy. Various versions have evolved over the years, sometimes by accident.</p>
  <a class="btn btn-blue" href="#">CONTACT US →</a>
</article>
<span class="about-ring"></span>

<section class="feedback">
  <div class="sec-head" style="left:160px;top:36px">
    <span class="ring" style="width:96px;height:96px"></span>
    <div>
      <h2 style="letter-spacing:0">Our Client Feedback</h2>
      <p style="width:520px">It is a long established fact that a reader will be distracted by the readable content of a page when looking at its layout.</p>
    </div>
  </div>
  <article class="quote" style="left:180px">
    <span class="photo" role="img" aria-label="Client portrait photo"></span>
    <p>It is a long established fact that a reader will be distracted by the readable content of a page when looking at its layout.</p>
    <h4>Marco Ellison</h4>
  </article>
  <article class="quote" style="left:480px">
    <span class="photo" role="img" aria-label="Client portrait photo"></span>
    <p>It is a long established fact that a reader will be distracted by the readable content of a page when looking at its layout.</p>
    <h4>Owen Caldwell</h4>
  </article>
  <article class="quote" style="left:780px">
    <span class="photo" role="img" aria-label="Client portrait photo"></span>
    <p>It is a long established fact that a reader will be distracted by the readable content of a page when looking at its layout.</p>
    <h4>Nadia Fenwick</h4>
  </article>
</section>

<section class="contact">
  <h2>LET'S GET IN TOUCH</h2>
  <div class="field" style="left:240px;top:130px;width:340px"><label>First Name*</label><span></span></div>
  <div class="field" style="left:600px;top:130px;width:340px"><label>Last Name*</label><span></span></div>
  <div class="field" style="left:240px;top:214px;width:340px"><label>Phone*</label><span style="height:40px"></span></div>
  <div class="field" style="left:600px;top:214px;width:340px"><label>E-mail*</label><span style="height:40px"></span></div>
  <div class="field" style="left:240px;top:294px;width:700px"><label>Message</label><span style="height:110px"></span></div>
  <a class="btn" href="#">SUBMIT</a>
</section>

<footer class="footer">
  <div class="brand"><span class="dot"></span>HARLOW RIDGE</div>
  <div class="abs" style="left:480px;top:56px">
    <h4>JOIN OUR NEWSLETTER</h4>
    <a class="btn btn-light" href="#" style="margin-top:14px;padding:8px 18px">SUBSCRIBE</a>
  </div>
  <div class="abs" style="left:720px;top:56px">
    <h4>ADDRESS</h4>
    <p>42 Calder Row<br>Brookhaven, NS 30418</p>
  </div>
  <div class="abs" style="left:900px;top:56px">
    <h4>FOLLOW US</h4>
    <div class="social"><i></i><i></i><i></i><i></i></div>
  </div>
  <p class="copy">© 2024 HARLOW RIDGE. ALL RIGHTS RESERVED</p>
</footer>

</body>
</html>
```